Step Marmalade - a dance school theatre production

We need a visually eye catching poster design which advertises our forthcoming theatre production "Step Marmalade" Sized A2

Our dance school is professional yet funky and modern, and we wish to portray this visually.

This has to be vibrant and colourful, with the school name and production name being the initial eye catching theme.

Our dance school name is the Welloby-Crane School of Dance

Our dance school offers a variety of dance styles including ballet,tap,street, jazz,rock and roll

Requirements
Must have
• "Step Marmalade" as the production name
www.wcschoolofdance.example
Ashgrove Lantern Theatre 01632 960417
30th September 2011-1st October 2011
price; £8 adults , £7 concessions
tickets available from the theatre box office
Nice to have
• an eye catching main image incorporated into the design?
Should not have
• no flowery fonts please

```html
<!DOCTYPE html>
<html lang="en">
<head>
<meta charset="utf-8">
<title>Step Marmalade – Welloby-Crane School of Dance</title>
<link rel="stylesheet" href="https://fonts.googleapis.com/css2?family=Nunito:wght@900&family=Varela+Round&display=swap">
<style>
  :root {
    --paper: #ffffff;
    --frame: #9a9a9a;
    --candy-red: #f0184f;
    --navy: #1c2384;
    --mint: #46e07a;
    --magenta: #ff3fa8;
    --orange: #ff6a3d;
    --sky: #6cc4ff;
    --cyan: #7fe8ff;
    --green: #6ff0a0;
    --blue-light: #a8dcff;
    --blue-deep: #2f5ae6;
  }
  html, body {
    margin: 0;
    width: 1200px;
    height: 1200px;
    overflow: hidden;
    background: var(--paper);
  }
  .stage {
    position: relative;
    width: 1000px;
    height: 1000px;
    transform: scale(1.2);
    transform-origin: 0 0;
    font-family: "Varela Round", "Helvetica Neue", Arial, sans-serif;
  }
  .poster {
    position: absolute;
    left: 165px;
    top: 25px;
    width: 832px;
    height: 943px;
    border: 1px solid var(--frame);
    box-sizing: border-box;
    background: var(--paper);
  }
  .shards, .dancer {
    position: absolute;
    left: 0;
    top: 0;
    width: 1000px;
    height: 1000px;
  }
  .diagonal {
    position: absolute;
    transform-origin: 0 0;
    white-space: nowrap;
  }
  .presents {
    left: 393px;
    top: 90px;
    transform: rotate(62deg);
    font-size: 21px;
    line-height: 1;
    color: var(--navy);
    text-transform: uppercase;
    letter-spacing: -0.5px;
  }
  .presents .accent { color: var(--mint); }
  .production-title {
    left: 348px;
    top: 262px;
    transform: rotate(52deg);
    font-family: "Nunito", "Arial Black", sans-serif;
    font-weight: 900;
    font-size: 44px;
    line-height: 1;
    letter-spacing: 0.5px;
    color: var(--candy-red);
    text-transform: uppercase;
    background: var(--paper);
    padding: 5px 14px 8px;
  }
  .venue {
    left: 186px;
    top: 350px;
    transform: rotate(50deg);
    font-size: 13px;
    line-height: 1.9;
    color: var(--mint);
    text-transform: uppercase;
  }
  .venue .phone { padding-left: 58px; }
  .dates {
    left: 648px;
    top: 338px;
    transform: rotate(-36deg);
    font-size: 23px;
    line-height: 1.25;
    color: var(--candy-red);
  }
  .tickets {
    left: 590px;
    top: 648px;
    transform: rotate(55deg);
    color: var(--navy);
    font-size: 17px;
    line-height: 1.15;
  }
  .tickets .label { text-transform: uppercase; }
  .tickets .box-office {
    display: block;
    font-size: 12.5px;
    color: var(--mint);
    font-style: italic;
  }
  .web-address {
    left: 234px;
    top: 782px;
    transform: rotate(-90deg);
    font-size: 10px;
    font-weight: bold;
    color: var(--candy-red);
  }
</style>
</head>
<body>
<div class="stage">
  <div class="poster"></div>

  <svg class="shards" viewBox="0 0 1000 1000" aria-hidden="true">
    <g opacity="0.75">
      <polygon points="300,140 430,150 350,390" fill="var(--magenta)"/>
      <polygon points="515,240 755,250 545,385" fill="var(--orange)"/>
      <polygon points="595,320 700,430 625,530" fill="var(--magenta)"/>
      <polygon points="250,420 560,440 430,590" fill="var(--sky)"/>
      <polygon points="195,555 475,430 455,565" fill="var(--green)"/>
      <polygon points="565,420 660,365 575,470" fill="var(--green)"/>
      <polygon points="245,590 330,630 285,740" fill="var(--magenta)"/>
      <polygon points="270,560 330,790 395,590" fill="var(--cyan)"/>
      <polygon points="450,570 600,790 420,705" fill="var(--sky)"/>
      <polygon points="380,610 475,770 505,560" fill="var(--green)"/>
    </g>
  </svg>

  <svg class="dancer" viewBox="0 0 1000 1000" role="img" aria-label="Illustrated silhouette of a tap dancer in a top hat, mid-step, in layered blue tones">
    <defs>
      <linearGradient id="dancer-tone" x1="0" y1="0" x2="0" y2="1">
        <stop offset="0" stop-color="var(--blue-light)"/>
        <stop offset="1" stop-color="var(--blue-deep)"/>
      </linearGradient>
    </defs>
    <rect x="350" y="95" width="180" height="810" rx="90" fill="url(#dancer-tone)" opacity="0.5"/>
  </svg>

  <div class="diagonal presents">Welloby-Crane School of Dance <span class="accent">Presents</span></div>
  <div class="diagonal production-title">Step Marmalade</div>

  <div class="diagonal venue">
    <div>Ashgrove Lantern Theatre</div>
    <div class="phone">01632 960417</div>
  </div>

  <div class="diagonal dates">30th September<br>to 01st October<br>2011</div>

  <div class="diagonal tickets">
    <span class="label">Price:</span> £8 adults, £7 concessions
    <span class="box-office">tickets available from the theatre box office</span>
  </div>

  <div class="diagonal web-address">www.wcschoolofdance.example</div>
</div>
</body>
</html>
```